Plakat-Design für Immobilienmakler
Zielgruppe
Wir sind Immobilienmakler
Aufgabenstellung
Benötigen die Datei für eine Schaufenstervollbeklebung.
Maße: Bx 1,99m, H 1,70m
Ist direkt in der Stadt an der Straße.
Soll schick, edel aussehen und unsere Leistungen aufzeigen.
z.B.
Lehnen Sie sich zurück wir kümmern uns um Ihre Immobilie!
oder
Wir haben den passenden Käufer für Ihre Immobilie!
- kaufen
- verkaufen
- makeln
- Home Staging
- Hausmeisterservice
Ihr Immobilienmakler in Gaildorf, Schwäbisch Hall, Backnang

```html
<!DOCTYPE html>
<html lang="de">
<head>
<meta charset="utf-8">
<title>Tal-Immobilien Brenner – Schaufensterplakat</title>
<link rel="stylesheet" href="https://fonts.googleapis.com/css2?family=Jost:wght@400;500;600&display=swap">
<style>
  :root{
    --navy:#12406b;
    --navy-deep:#0f3a62;
    --gold:#c39a3a;
    --white:#ffffff;
  }
  html,body{margin:0;padding:0;width:1200px;height:1200px;overflow:hidden;background:var(--white);}
  .poster{position:absolute;left:254px;top:296px;width:669px;height:571px;overflow:hidden;}
  .poster-inner{position:absolute;left:0;top:0;width:1071px;height:914px;transform:scale(0.625);transform-origin:0 0;font-family:'Jost',sans-serif;}
  .scene{position:absolute;inset:0;width:1071px;height:914px;}
  .brand-top{position:absolute;left:24px;top:44px;width:170px;font-size:27px;line-height:31px;font-weight:600;color:var(--navy);}
  .brand-badge{position:absolute;left:693px;top:486px;width:160px;text-align:center;font-size:24px;line-height:28px;font-weight:600;color:var(--navy);}
  .headline{position:absolute;left:58px;top:580px;margin:0;color:var(--white);font-weight:400;font-size:48px;line-height:67px;word-spacing:10px;letter-spacing:.5px;}
  .headline .accent{color:var(--gold);font-size:68px;font-weight:400;word-spacing:0;}
  .subline{position:absolute;left:60px;top:788px;margin:0;color:var(--white);font-size:32px;line-height:44px;font-weight:400;word-spacing:8px;letter-spacing:.5px;}
  .services{position:absolute;left:626px;top:628px;color:var(--white);}
  .services h2{margin:0 0 6px;font-size:28px;font-weight:400;letter-spacing:.5px;word-spacing:6px;}
  .services ul{list-style:none;margin:0;padding:0 0 0 142px;}
  .services li{position:relative;font-size:24px;line-height:44px;font-weight:500;word-spacing:5px;}
  .services li svg{position:absolute;left:-50px;top:10px;width:34px;height:26px;}
</style>
</head>
<body>
<div class="poster">
  <div class="poster-inner">
    <svg class="scene" viewBox="0 0 1071 914" xmlns="http://www.w3.org/2000/svg">
      <defs>
        <linearGradient id="photoTone" x1="0" y1="0" x2="1" y2="0">
          <stop offset="0" stop-color="#dfe3e8"/>
          <stop offset=".45" stop-color="#eeeef1"/>
          <stop offset=".72" stop-color="#d9d6de"/>
          <stop offset="1" stop-color="#7fa7cf"/>
        </linearGradient>
        <linearGradient id="photoGreens" x1="0" y1="0" x2="0" y2="1">
          <stop offset="0" stop-color="#7a9a52" stop-opacity="0"/>
          <stop offset=".55" stop-color="#7a9a52" stop-opacity="0"/>
          <stop offset=".85" stop-color="#6f9444" stop-opacity=".85"/>
          <stop offset="1" stop-color="#5c7f38"/>
        </linearGradient>
        <linearGradient id="photoSky" x1="0" y1="0" x2="0" y2="1">
          <stop offset="0" stop-color="#9dbcdc" stop-opacity=".75"/>
          <stop offset=".3" stop-color="#9dbcdc" stop-opacity="0"/>
        </linearGradient>
        <linearGradient id="peopleTone" x1="0" y1="0" x2="0" y2="1">
          <stop offset="0" stop-color="#b4b4b4"/>
          <stop offset=".5" stop-color="#8c8c8c"/>
          <stop offset="1" stop-color="#222"/>
        </linearGradient>
        <linearGradient id="houseTone" x1="0" y1="0" x2="1" y2="1">
          <stop offset="0" stop-color="#1f4a75"/>
          <stop offset=".55" stop-color="#f1e3b0"/>
          <stop offset="1" stop-color="#d9c283"/>
        </linearGradient>
        <linearGradient id="panel" x1="0" y1="0" x2="1" y2="0">
          <stop offset="0" stop-color="#12406b"/>
          <stop offset="1" stop-color="#0f3a62"/>
        </linearGradient>
      </defs>
      <g role="img" aria-label="Foto eines modernen weißen Einfamilienhauses mit Balkon vor blauem Himmel, umgeben von Grünpflanzen">
        <rect width="1071" height="914" fill="url(#photoTone)"/>
        <rect width="1071" height="914" fill="url(#photoSky)"/>
        <rect width="1071" height="914" fill="url(#photoGreens)"/>
      </g>
      <path d="M0,517 Q250,430 500,440 Q820,455 1071,700 L1071,914 L0,914 Z" fill="url(#panel)"/>
      <path d="M0,560 Q250,470 520,472 Q820,480 1071,722" fill="none" stroke="var(--gold)" stroke-width="9"/>
      <circle cx="258" cy="437" r="143" fill="url(#peopleTone)" stroke="var(--gold)" stroke-width="11" role="img" aria-label="Foto des Maklerteams: eine Frau und ein Mann in dunklen Anzügen"/>
      <circle cx="538" cy="464" r="104" fill="url(#houseTone)" stroke="var(--gold)" stroke-width="11" role="img" aria-label="Bild eines Hauses im warmen Licht"/>
      <circle cx="773" cy="517" r="88" fill="var(--white)" stroke="var(--gold)" stroke-width="11"/>
    </svg>
    <div class="brand-top">Tal-Immobilien Brenner</div>
    <div class="brand-badge">Tal-Immobilien Brenner</div>
    <h1 class="headline">Wir haben den<br>passenden Käufer<br>für Ihre <span class="accent">Immobilie!</span></h1>
    <p class="subline">Ihr Immobilienmakler<br>in Gaildorf, Schwäbisch Hall, Backnang</p>
    <div class="services">
      <h2>UNSERE LEISTUNGEN:</h2>
      <ul>
        <li><svg viewBox="0 0 34 26"><path d="M2,13 L12,23 L32,3" fill="none" stroke="var(--gold)" stroke-width="3.5"/></svg>kaufen</li>
        <li><svg viewBox="0 0 34 26"><path d="M2,13 L12,23 L32,3" fill="none" stroke="var(--gold)" stroke-width="3.5"/></svg>verkaufen</li>
        <li><svg viewBox="0 0 34 26"><path d="M2,13 L12,23 L32,3" fill="none" stroke="var(--gold)" stroke-width="3.5"/></svg>makeln</li>
        <li><svg viewBox="0 0 34 26"><path d="M2,13 L12,23 L32,3" fill="none" stroke="var(--gold)" stroke-width="3.5"/></svg>Home Staging</li>
        <li><svg viewBox="0 0 34 26"><path d="M2,13 L12,23 L32,3" fill="none" stroke="var(--gold)" stroke-width="3.5"/></svg>Hausmeisterservice</li>
      </ul>
    </div>
  </div>
</div>
</body>
</html>
```